Upscale business cards needed for Board of Directors

We need professional business cards created for members of our family business Board of Directors. We would like these relatively simple and straightforward, but also with a unique element to set them apart. Probably stick with neutral and simple colors - white, grey etc. We need space for the traditional elements, including name, title, address, email/phone number. And we will be creating several from this template so it needs to be template that is easy to switch information in and out of.
Business
See description

```html
<!DOCTYPE html>
<html lang="en">
<head>
<meta charset="utf-8">
<title>Business Card – Harborline Holdings</title>
<link rel="stylesheet" href="https://fonts.googleapis.com/css2?family=Saira:wght@300;400;700&display=swap">
<style>
  :root {
    --paper: #fbfbfb;
    --paper-shade: #f1f2f2;
    --ink: #16181a;
    --gold: #8e8445;
    --slate: #4c5858;
    --contact: #56615f;
  }
  html, body {
    margin: 0;
    padding: 0;
    width: 1200px;
    height: 1000px;
    overflow: hidden;
    background: var(--paper);
  }
  .card {
    position: relative;
    width: 1200px;
    height: 1000px;
    overflow: hidden;
    font-family: "Saira", sans-serif;
  }
  .card__texture {
    position: absolute;
    inset: 0;
    background: radial-gradient(ellipse at center, var(--paper) 0%, var(--paper-shade) 100%);
  }
  .brand {
    position: absolute;
    left: 157px;
    top: 300px;
    margin: 0;
    color: var(--ink);
    font-size: 38px;
    font-weight: 700;
    text-transform: uppercase;
    letter-spacing: 1px;
    line-height: 1;
    white-space: nowrap;
  }
  .person {
    position: absolute;
    top: 462px;
    left: 0;
    width: 1200px;
    text-align: center;
    text-transform: uppercase;
    font-weight: 700;
    line-height: 1;
  }
  .person__name {
    margin: 0;
    font-size: 32px;
    color: var(--gold);
    letter-spacing: 0.5px;
  }
  .person__role {
    margin: 8px 0 0;
    font-size: 24px;
    color: var(--slate);
    letter-spacing: 0.5px;
  }
  .contacts {
    position: absolute;
    top: 612px;
    left: 0;
    width: 1200px;
    margin: 0;
    padding: 0;
    list-style: none;
  }
  .contact {
    position: absolute;
    top: 0;
    width: 340px;
    margin-left: -170px;
    text-align: center;
  }
  .contact--phone { left: 273px; }
  .contact--email { left: 599px; }
  .contact--address { left: 934px; }
  .contact__icon {
    display: block;
    height: 46px;
    margin: 0 auto;
    fill: var(--gold);
  }
  .contact__text {
    display: block;
    margin-top: 38px;
    font-size: 27px;
    font-weight: 300;
    color: var(--contact);
    line-height: 1.2;
    white-space: nowrap;
  }
</style>
</head>
<body>
  <main class="card">
    <div class="card__texture" role="img" aria-label="Faint light grey triangle pattern background"></div>

    <p class="brand">Harborline Holdings</p>

    <section class="person">
      <h1 class="person__name">Marcus Bell</h1>
      <p class="person__role">Chief Technology Officer</p>
    </section>

    <ul class="contacts">
      <li class="contact contact--phone">
        <svg class="contact__icon" viewBox="0 0 40 46" width="40" aria-hidden="true">
          <path d="M9 3c2-2 4-1 5 1l4 7c1 2 0 3-1 4l-2 2c1 3 4 7 7 9l2-2c1-1 3-1 4 0l6 5c2 1 2 3 0 5l-3 3c-3 3-9 1-15-5C9 26 5 18 6 10z"/>
          <path d="M4 30c-3 3-2 8 2 10 3 2 7 1 9-1l3-3" fill="none" stroke="var(--gold)" stroke-width="3.5" stroke-linecap="round"/>
        </svg>
        <span class="contact__text">+ 00 555 210 348</span>
      </li>
      <li class="contact contact--email">
        <svg class="contact__icon" viewBox="0 0 44 46" width="44" aria-hidden="true">
          <rect x="1" y="12" width="42" height="30" rx="3"/>
          <path d="M6 16l16 13 16-13M6 38l12-10M38 38l-12-10" fill="none" stroke="var(--paper)" stroke-width="2.5" stroke-linecap="round"/>
        </svg>
        <span class="contact__text">m.bell@harborline.it</span>
      </li>
      <li class="contact contact--address">
        <svg class="contact__icon" viewBox="0 0 30 46" width="30" aria-hidden="true">
          <path d="M15 2C7 2 1 8 1 15c0 8 8 14 11 29h6C21 29 29 23 29 15 29 8 23 2 15 2z"/>
          <circle cx="15" cy="15" r="5.5" fill="var(--paper)"/>
        </svg>
        <span class="contact__text">48 Quay Street</span>
      </li>
    </ul>
  </main>
</body>
</html>
```